Organic lawn care

take the same sign as the mosquito sign, only instead of the mosquito image have the red circle and line cross out the text of "chemicals". Have the sign say "this lawn receives ORGANIC grass treatments" "instantly SAFE for people and pets"

Lawn Care

```html
<!DOCTYPE html>
<html lang="en">
<head>
<meta charset="utf-8">
<title>Organic Lawn Care Sign</title>
<link href="https://fonts.googleapis.com/css2?family=Roboto:wght@700;900&display=swap" rel="stylesheet">
<style>
  :root {
    --sky-top: #4f8fd0;
    --sky-mid: #a9cdef;
    --haze: #ffffff;
    --grass-light: #8fd14a;
    --grass-dark: #3f8f1c;
    --ink: #111111;
    --organic-green: #3a9a3a;
    --safe-red: #d8262e;
    --stamp-red: #d8262e;
    --photo-warm: #c9b7a3;
    --photo-cool: #9fc4e6;
  }
  html, body {
    margin: 0;
    padding: 0;
    overflow: hidden;
    background: #ffffff;
  }
  .sign {
    position: relative;
    width: 1200px;
    height: 571px;
    overflow: hidden;
    font-family: "Roboto", Arial, sans-serif;
    background: linear-gradient(180deg, var(--sky-top) 0%, var(--sky-mid) 9%, var(--haze) 22%, var(--haze) 62%, var(--sky-mid) 82%, var(--sky-top) 100%);
  }
  .family-photo {
    position: absolute;
    left: 480px;
    top: 20px;
    width: 690px;
    height: 470px;
    border-radius: 40px 40px 0 0;
    background: radial-gradient(ellipse at 60% 55%, var(--photo-warm) 0%, rgba(201,183,163,0.7) 45%, rgba(159,196,230,0) 75%);
  }
  .headline {
    position: absolute;
    left: 62px;
    top: 52px;
    margin: 0;
    color: var(--ink);
    font-weight: 900;
    line-height: 1;
  }
  .headline .lead {
    display: block;
    font-size: 40px;
    letter-spacing: 0.5px;
  }
  .headline .organic {
    display: block;
    margin-top: 8px;
    margin-left: -4px;
    font-size: 136px;
    color: var(--organic-green);
    letter-spacing: 1px;
    line-height: 0.9;
  }
  .headline .tail {
    display: block;
    margin-top: 14px;
    font-size: 44px;
    font-weight: 700;
    letter-spacing: 0.5px;
  }
  .safety {
    position: absolute;
    left: 62px;
    top: 340px;
    margin: 0;
    color: var(--ink);
    font-size: 32px;
    font-weight: 700;
    line-height: 1.15;
  }
  .safety .safe {
    color: var(--safe-red);
    font-weight: 900;
  }
  .stamp {
    position: absolute;
    left: 508px;
    top: 328px;
    width: 214px;
    height: 214px;
    z-index: 2;
  }
  .lawn {
    position: absolute;
    left: 0;
    bottom: 0;
    width: 1200px;
    height: 120px;
    z-index: 1;
  }
</style>
</head>
<body>
  <main class="sign">
    <div class="family-photo" role="img" aria-label="Photo of a smiling family with a child and a black and white puppy lying on the lawn"></div>

    <h1 class="headline">
      <span class="lead">THIS LAWN RECEIVES</span>
      <span class="organic">ORGANIC</span>
      <span class="tail">GRASS TREATMENTS</span>
    </h1>

    <p class="safety">INSTANTLY <span class="safe">SAFE</span> FOR<br>PEOPLE AND PETS</p>

    <svg class="lawn" viewBox="0 0 1200 120" role="img" aria-label="Photo of fresh green grass along the bottom edge">
      <defs>
        <linearGradient id="grassFill" x1="0" y1="0" x2="0" y2="1">
          <stop offset="0" stop-color="var(--grass-light)"/>
          <stop offset="1" stop-color="var(--grass-dark)"/>
        </linearGradient>
      </defs>
      <path fill="url(#grassFill)" d="M0 30 L20 10 L40 28 L60 6 L85 26 L110 4 L135 24 L160 8 L185 26 L210 2 L240 22 L265 8 L290 28 L320 6 L350 24 L380 10 L410 28 L440 4 L470 24 L500 12 L530 30 L560 8 L590 26 L620 14 L650 32 L680 10 L710 28 L740 14 L770 34 L800 12 L830 30 L860 16 L890 34 L920 12 L950 30 L980 18 L1010 36 L1040 14 L1070 30 L1100 12 L1130 28 L1160 10 L1200 26 L1200 120 L0 120 Z"/>
    </svg>

    <svg class="stamp" viewBox="0 0 214 214" aria-label="100% chemical free">
      <g transform="rotate(-22 107 107)">
        <circle cx="107" cy="107" r="98" fill="#ffffff"/>
        <circle cx="107" cy="107" r="94" fill="none" stroke="var(--stamp-red)" stroke-width="9"/>
        <text x="107" y="92" text-anchor="middle" font-family="Roboto, Arial, sans-serif" font-weight="900" font-size="54" fill="var(--stamp-red)">100%</text>
        <text x="107" y="130" text-anchor="middle" font-family="Roboto, Arial, sans-serif" font-weight="900" font-size="33" fill="var(--stamp-red)">CHEMICAL</text>
        <text x="107" y="164" text-anchor="middle" font-family="Roboto, Arial, sans-serif" font-weight="900" font-size="33" fill="var(--stamp-red)">FREE!</text>
      </g>
    </svg>
  </main>
</body>
</html>
```